Bref créative
New Corporate Website - Blue Falcons
Blue Falcons - Marketing & Lead Generation
Marketing
Does not yet exist
Blue Falcons is a new Marketing and Sales Lead generation agency specializing in helping companies analyze, pursue and close sales opportunities generated via the Internet. We provide access to our exclusive Blue Falcon Striker platform for capturing and pursing sales opportunities generated via the online platform.
I'd like to showcase a lot of red on this website. This is a new website for a new company we are starting.
The website is to feature both our online web software as well as our consulting services.
High Tech
Red (#aa0000)
Grey (#cccccc)
Verdana
Century Gothic
top
http://www.vortelix.com
http://www.brinaxo.com/en
http://www.quombrel.com
The page should include links for
Navigation
- About Blue Falcons
- Services & Solutions
- Results
- News & Announcements
- Contact Us
Also, an area for current customer's to login
please incorporate the logo of the man riding the horse backwards.

```html
<!DOCTYPE html>
<html lang="en">
<head>
<meta charset="utf-8">
<title>Blue Falcons – Marketing &amp; Lead Generation</title>
<link rel="stylesheet" href="https://fonts.googleapis.com/css2?family=Tenor+Sans&family=Open+Sans:ital,wght@0,400;0,700;1,400&display=swap">
<style>
:root{
  --red:#aa0000;
  --red-dark:#7a0000;
  --red-deep:#5a0000;
  --red-bright:#c40d0d;
  --pink:#f6c7c7;
  --white:#ffffff;
  --grey:#cccccc;
  --grey-light:#dadada;
  --grey-text:#6a6a6a;
  --ink:#2a0000;
}
*{box-sizing:border-box;margin:0;padding:0}
html,body{width:1200px;height:821px;overflow:hidden}
body{
  position:relative;
  font-family:Verdana,"Open Sans",sans-serif;
  background:linear-gradient(180deg,var(--red-dark) 0,var(--red) 72px,var(--red) 700px,var(--red-dark) 744px,var(--grey) 744px,var(--grey-light) 821px);
  color:var(--white);
}
.site-nav{position:absolute;top:0;left:0;width:1200px;height:72px}
.site-nav a{position:absolute;top:14px;color:var(--white);text-decoration:none;font-size:18px;letter-spacing:.2px}
.nav-about{left:163px}.nav-services{left:384px}.nav-news{left:679px}.nav-contact{left:941px}

.page-panel{
  position:absolute;left:125px;top:79px;width:948px;height:636px;
  background:radial-gradient(ellipse at 50% 40%,var(--red-bright) 0,var(--red) 55%,var(--red-dark) 100%);
  border-top:2px solid #e04a4a;
  box-shadow:0 6px 22px rgba(0,0,0,.55);
}
.brand{position:absolute;left:34px;top:12px;font-family:"Tenor Sans",sans-serif;font-size:44px;color:var(--white)}

.hero{position:absolute;left:0;top:70px;width:948px;height:247px;
  background:linear-gradient(90deg,#f4f4f4 0,#e7dcdc 30%,var(--red-bright) 52%,var(--red) 100%)}
.hero-visual{position:absolute;left:0;top:0;width:470px;height:225px;
  background:linear-gradient(90deg,#ececee 0,#d9d9dd 55%,#d8c4c4 80%,rgba(215,180,180,0) 100%)}
.hero-title{position:absolute;left:482px;top:14px;font-family:"Tenor Sans",sans-serif;font-weight:400;font-size:46px;line-height:58px;color:#f7e6e6}
.hero-quote{position:absolute;left:486px;top:134px;width:430px;font-style:italic;font-size:18px;line-height:22px;color:var(--pink)}
.hero-bar{position:absolute;left:0;bottom:0;width:948px;height:22px;background:linear-gradient(180deg,#b5b5b5,#8d8d8d)}
.hero-bar svg{position:absolute;left:0;top:-12px}

.login{position:absolute;left:36px;top:340px;width:240px}
.section-title{font-family:"Open Sans",Verdana,sans-serif;font-weight:700;font-size:29px;color:var(--white)}
.login-field{display:flex;align-items:center;margin-top:14px;font-size:13px;font-weight:700}
.login-field label{width:86px}
.login-field input{width:130px;height:18px;border:1px solid var(--red-deep);background:var(--white)}
.login-actions{margin:12px 0 0 86px;display:flex;gap:6px}
.login-actions button{height:20px;padding:0 8px;font-family:inherit;font-size:12px;color:var(--white);background:var(--red);border:1px solid var(--pink)}
.login-mark{position:absolute;left:70px;top:150px;display:flex;align-items:center;gap:8px;font-size:16px;font-weight:700;color:var(--ink)}
.login-mark span.dot{width:14px;height:14px;border-radius:50%;background:var(--ink)}

.news{position:absolute;left:297px;top:340px;width:650px}
.news-list{list-style:none;margin-top:8px}
.news-item{font-size:12px;line-height:15px;color:var(--pink);font-style:italic;margin-bottom:14px}
.news-item time{font-style:normal;font-weight:700;color:var(--white);margin-right:8px}
.news-item.plain{font-style:normal;color:var(--white)}

.site-footer{position:absolute;top:755px;left:127px;width:946px;font-size:11px;color:var(--grey-text)}
.footer-links{position:absolute;right:0;top:0;display:flex;gap:14px}
.footer-links a{color:var(--grey-text);text-decoration:none}
</style>
</head>
<body>
<nav class="site-nav">
  <a class="nav-about" href="#">About Blue Falcons</a>
  <a class="nav-services" href="#">Services &amp; Solutions Results</a>
  <a class="nav-news" href="#">News &amp; Announcements</a>
  <a class="nav-contact" href="#">Contact Us</a>
</nav>

<main class="page-panel">
  <div class="brand">Blue Falcons</div>

  <section class="hero">
    <div class="hero-visual" role="img" aria-label="Photo of a field of grey spheres with one red sphere standing out"></div>
    <h1 class="hero-title">Blue Falcons<br>Lead Generation</h1>
    <p class="hero-quote">"Lorem ipsum dolor sit amet, consectetur adipisicing elit, sed do eiusmod tempor incididunt ut labore et dolore magna aliqua."</p>
    <div class="hero-bar">
      <svg width="948" height="34" viewBox="0 0 948 34">
        <path d="M0 12 H820 Q850 12 860 22 H948 V34 H0Z" fill="#9a9a9a"/>
        <path d="M820 12 Q850 12 860 22" stroke="#fff" stroke-width="2" fill="none"/>
        <g fill="#5e5e5e"><circle cx="872" cy="24" r="5"/><circle cx="888" cy="24" r="5"/><circle cx="904" cy="24" r="5"/><circle cx="920" cy="24" r="5"/><circle cx="936" cy="24" r="5"/></g>
      </svg>
    </div>
  </section>

  <section class="login">
    <h2 class="section-title">User login</h2>
    <div class="login-field"><label for="user">User name:</label><input id="user" type="text"></div>
    <div class="login-field"><label for="pass">Password:</label><input id="pass" type="password"></div>
    <div class="login-actions"><button type="button">Login</button><button type="button">Register</button></div>
    <div class="login-mark"><span class="dot"></span>Blue Falcons</div>
  </section>

  <section class="news">
    <h2 class="section-title">News &amp; Announcements</h2>
    <ul class="news-list">
      <li class="news-item"><time>27 07 2011</time>"Lorem ipsum dolor sit amet, consectetur adipisicing elit, sed do eiusmod tempor incididunt ut labore et dolore magna aliqua. Ut enim ad minim veniam, quis nostrud exercitation ullamco laboris nisi ut aliquip ex ea commodo consequat."</li>
      <li class="news-item"><time>27 07 2011</time>Duis aute irure dolor in reprehenderit in voluptate velit esse cillum dolore eu fugiat nulla pariatur. Excepteur sint occaecat cupidatat non proident, sunt in culpa qui officia deserunt mollit anim id est laborum.</li>
      <li class="news-item"><time>26 07 2011</time>The standard chunk of Lorem Ipsum used since the 1500s is reproduced below for those interested. Sections 1.10.32 and 1.10.33 from "de Finibus Bonorum et Malorum" by Varro Lentus are also reproduced in their exact original form, accompanied by English versions from the 1914 translation by J. Orlwen.</li>
      <li class="news-item plain"><time>25 07 2011</time>1.10.32 and 1.10.33 of "de Finibus Bonorum et Malorum" (The Extremes of Good and Evil) by Varro Lentus, written in 45 BC.</li>
    </ul>
  </section>
</main>

<footer class="site-footer">
  <span>Copyright © 2011 Blue Falcons. All Rights Reserved.</span>
  <nav class="footer-links">
    <a href="#">About Blue Falcons</a><a href="#">Services &amp; Solutions</a><a href="#">Results</a><a href="#">News &amp; Announcements</a><a href="#">Contact Us</a>
  </nav>
</footer>
</body>
</html>
```